Cleaning Service Company In need of Good Web presence.

The company is a cleaning service company which provides professional staff and service for cleaning. This is a project to build a site that is both solid and a strong recognition of our organization. It is supposed to show quality, cleanliness, professionalism. The use of images and art for imagery is all good just to have a site that is consistent and solid. There might be a chance to make stationary, logo and business cars if someone feels they can build a brand that is consistent. The image we are going for is clean solid and to stand out. Finally stationary should not be expensive to print.

Current logo is attached and can be used or can be made more creative.

Target Market(s)

Corporate and Government entities, that will feel that this company has a brand that sets it apart from the rest. The company is new so the modification of the logo will not be an issue if a more solid brand come out of this project. The idea is to have a clean consistent product that stands our from others in terms of website, stationary, etc

Industry/Entity Type

Cleaning Service

Contact Information for Business Card

P.O.Box 41967
Riffa
Kingdom of Bahrain

Logo Text

Maple Ridge Solutions

Number of Pages Required

4 page

Font styles to use
Sans Serif

Colors
abd036
cadf82
eaf2ce
9bcb3b

Requirements
Must have
• Green Color to be used in order to stick to the name. Also the creativity and boldness in an elegant manner.
Nice to have
• Arabic name of company
• نوفا بلو للحلول ذ.م.م
• if cannot be put at least make a location should be chosen
• Also could be a bit of 3D given to the logo if it could stay elegent.
Should not have
• Should not show people cleaning.

```html
<!DOCTYPE html>
<html lang="en">
<head>
<meta charset="utf-8">
<title>Maple Ridge Solutions W.L.L</title>
<link href="https://fonts.googleapis.com/css2?family=Open+Sans:wght@300;400;600;700&family=Amiri:wght@700&display=swap" rel="stylesheet">
<style>
  :root{
    --green:#9bcb3b;
    --green-strong:#abd036;
    --green-soft:#cadf82;
    --green-pale:#eaf2ce;
    --ink:#444;
    --muted:#888;
    --grey-band:#f3f3f3;
    --white:#fff;
  }
  *{box-sizing:border-box;margin:0;padding:0}
  html,body{width:1200px;height:2476px;overflow:hidden}
  body{font-family:"Open Sans",Arial,sans-serif;color:var(--ink);background:var(--white);position:relative}

  .site-header{position:absolute;top:0;left:0;width:1200px;height:140px;background:var(--white)}
  .brand{position:absolute;left:100px;top:10px;display:flex;align-items:center;gap:14px}
  .brand-mark{width:120px;height:120px;border-radius:50%;background:var(--green);display:flex;align-items:center;justify-content:center;color:var(--white);font-weight:700;font-size:17px;text-align:center;line-height:1.25;padding:12px}
  .main-nav{position:absolute;right:100px;top:56px;display:flex;gap:56px;font-size:17px}
  .main-nav a{color:var(--ink);text-decoration:none}
  .main-nav a.active{color:var(--green)}

  .hero{position:absolute;top:140px;left:0;width:1200px;height:590px;overflow:hidden}
  .hero-photo{position:absolute;inset:0;background:linear-gradient(180deg,#6fae3a 0%,#3f8a3c 45%,#2f7a45 100%)}
  .hero-title{position:absolute;top:150px;left:0;width:1200px;text-align:center;font-family:"Amiri",serif;font-size:84px;color:var(--white);direction:rtl}
  .hero-arrow{position:absolute;top:190px;width:50px;height:50px;border-radius:50%;background:rgba(0,0,0,.35)}
  .hero-arrow.left{left:0}
  .hero-arrow.right{right:0}
  .hero-curve{position:absolute;bottom:0;left:0;width:1200px;height:160px}

  .welcome{position:absolute;top:750px;left:100px;width:1000px;height:320px}
  .section-title{font-weight:300;font-size:38px;color:var(--ink);line-height:1.3}
  .welcome .section-title{margin-top:4px;width:570px;font-size:30px;white-space:nowrap}
  .welcome-text{position:absolute;left:0;top:62px;width:560px}
  .body-copy{font-size:14px;line-height:1.75;color:var(--muted)}
  .btn-outline{display:inline-block;padding:10px 30px;border:2px solid var(--green);border-radius:30px;color:var(--green);font-size:15px;font-weight:600;letter-spacing:.5px}
  .welcome .btn-outline{position:absolute;left:0;top:258px}
  .photo-frame{position:absolute;background:var(--white);box-shadow:0 2px 8px rgba(0,0,0,.18);padding:8px}
  .photo-frame .fill{width:100%;height:100%}
  .welcome .photo-frame{left:600px;top:0;width:390px;height:290px}

  .services{position:absolute;top:1090px;left:0;width:1200px;height:550px;background:var(--grey-band);text-align:center}
  .services .section-title{padding-top:64px}
  .service-list{display:flex;justify-content:center;gap:120px;margin-top:52px}
  .service{width:240px}
  .service-icon{width:170px;height:170px;margin:0 auto;border-radius:50%;background:var(--green);border:6px solid var(--green-pale);display:flex;align-items:center;justify-content:center}
  .service h3{margin-top:26px;font-size:17px;font-weight:700;color:#333}
  .service p{margin-top:10px;font-size:12px;line-height:1.6;color:var(--muted)}

  .govt{position:absolute;top:1690px;left:100px;width:1000px;height:400px}
  .govt .section-title{margin-top:30px;width:540px;font-size:40px}
  .govt .body-copy{margin-top:20px;width:540px}
  .btn-solid{position:absolute;left:0;top:320px;padding:10px 34px;border-radius:30px;background:var(--green);color:var(--white);font-size:14px;font-weight:600}
  .govt .photo-frame{left:560px;top:0;width:430px;height:292px}

  .site-footer{position:absolute;top:2140px;left:0;width:1200px;height:336px;background:var(--green);color:var(--white)}
  .footer-cols{position:absolute;top:40px;left:100px;width:1000px;display:flex}
  .footer-col{font-size:13px;line-height:2}
  .footer-col h4{font-size:14px;font-weight:700;letter-spacing:.5px;margin-bottom:4px}
  .col-links{width:188px}
  .col-more{width:252px;padding-top:26px}
  .col-info{width:240px}
  .col-news{width:320px}
  .newsletter{display:flex;margin-top:10px}
  .newsletter .field{width:220px;height:42px;background:var(--white);color:#aaa;font-size:12px;padding:12px}
  .newsletter .send{height:42px;padding:0 16px;background:#7aa82a;font-size:12px;font-weight:700;line-height:42px}
  .social{display:flex;gap:10px;margin-top:18px}
  .social span{width:36px;height:36px;border-radius:50%;background:#7aa82a}
  .footer-bottom{position:absolute;bottom:0;left:100px;width:1000px;height:56px;border-top:1px solid rgba(255,255,255,.5);display:flex;justify-content:space-between;align-items:center;font-size:11px}
</style>
</head>
<body>

<header class="site-header">
  <div class="brand"><div class="brand-mark">Maple Ridge Solutions</div></div>
  <nav class="main-nav">
    <a class="active" href="#">Home</a>
    <a href="#">About Us</a>
    <a href="#">Our Services</a>
    <a href="#">Products</a>
    <a href="#">Quote</a>
    <a href="#">Contact Us</a>
  </nav>
</header>

<section class="hero">
  <div class="hero-photo" role="img" aria-label="Green-tinted aerial view of a coastal city skyline with a sail-shaped hotel tower"></div>
  <h1 class="hero-title">نوفا بلو للحلول ذ.م.م</h1>
  <span class="hero-arrow left"></span>
  <span class="hero-arrow right"></span>
  <svg class="hero-curve" viewBox="0 0 1200 160" preserveAspectRatio="none">
    <path d="M0 20 Q600 240 1200 20 L1200 160 L0 160 Z" fill="#fff"/>
  </svg>
</section>

<section class="welcome">
  <h2 class="section-title">Welcome to Maple Ridge Solutions W.L.L</h2>
  <p class="welcome-text body-copy">Lorem ipsum dolor sit amet, consectetur adipiscing elit, sed do eiusmod tempor incididunt ut labore et dolore magna aliqua. Ut enim ad minim veniam, quis nostrud exercitation ullamco laboris nisi ut aliquip ex ea commodo consequat. Duis aute irure dolor in reprehenderit in voluptate velit esse cillum dolore eu fugiat nulla pariatur. Excepteur sint occaecat cupidatat non proident, sunt in culpa qui officia deserunt mollit anim id est laborum.</p>
  <span class="btn-outline">READ MORE</span>
  <div class="photo-frame"><div class="fill" role="img" aria-label="Business team standing in front of a modern city skyline" style="background:linear-gradient(180deg,#d9e6ee,#b7c4b0)"></div></div>
</section>

<section class="services">
  <h2 class="section-title">Our Services</h2>
  <div class="service-list">
    <div class="service">
      <div class="service-icon"><svg width="70" height="80" viewBox="0 0 70 80"><path d="M20 8h22v10H20zM26 18h12v8H26zM18 26h28l6 10v40H12V36z" fill="#fff"/></svg></div>
      <h3>DRY CLEANING</h3>
      <p>Sed ut perspiciatis unde omnis iste natus error sit voluptatem accusantium doloremque laudantium, totam rem aperiam, eaque ipsa quae ab illo inventore veritatis.</p>
    </div>
    <div class="service">
      <div class="service-icon"><svg width="80" height="80" viewBox="0 0 80 80"><circle cx="34" cy="46" r="24" fill="#fff"/><path d="M52 30 L70 8" stroke="#fff" stroke-width="5"/></svg></div>
      <h3>VACUUM CLEANING</h3>
      <p>Sed ut perspiciatis unde omnis iste natus error sit voluptatem accusantium doloremque laudantium, totam rem aperiam, eaque ipsa quae ab illo inventore veritatis.</p>
    </div>
    <div class="service">
      <div class="service-icon"><svg width="76" height="80" viewBox="0 0 76 80"><path d="M10 30h56l-6 44H16z" fill="#fff"/><path d="M20 30 Q38 6 56 30" stroke="#fff" stroke-width="4" fill="none"/></svg></div>
      <h3>OTHERS CLEANING</h3>
      <p>Sed ut perspiciatis unde omnis iste natus error sit voluptatem accusantium doloremque laudantium, totam rem aperiam, eaque ipsa quae ab illo inventore veritatis.</p>
    </div>
  </div>
</section>

<section class="govt">
  <h2 class="section-title">We Serve the Govt Agencies &amp; Office in their Cleaning.</h2>
  <p class="body-copy">Lorem ipsum dolor sit amet, consectetur adipiscing elit, sed do eiusmod tempor incididunt ut labore et dolore magna aliqua. Ut enim ad minim veniam, quis nostrud exercitation ullamco laboris nisi ut aliquip ex ea commodo consequat.</p>
  <span class="btn-solid">READ MORE</span>
  <div class="photo-frame"><div class="fill" role="img" aria-label="Bright white living room with a sofa and a cleaning machine on the floor" style="background:linear-gradient(180deg,#eef0f0,#c9ccc8)"></div></div>
</section>

<footer class="site-footer">
  <div class="footer-cols">
    <div class="footer-col col-links">
      <h4>USEFUL LINKS</h4>
      Home<br>About Us<br>Our Services<br>Products<br>Quote
    </div>
    <div class="footer-col col-more">
      Testimonials<br>Contact Us<br>Terms &amp; Conditions<br>Privacy Policy<br>FAQ
    </div>
    <div class="footer-col col-info">
      <h4>INFORMATION</h4>
      Specials<br>My Account<br>My Cart<br>Blog<br>Site Map
    </div>
    <div class="footer-col col-news">
      <h4>JOIN OUR MAILING LIST</h4>
      Sign up for news and offers to our mailing list.
      <div class="newsletter"><span class="field">Your email address</span><span class="send">SUBSCRIBE</span></div>
      <div class="social"><span></span><span></span><span></span><span></span></div>
    </div>
  </div>
  <div class="footer-bottom">
    <span>© 2017 MAPLE RIDGE SOLUTIONS W.L.L. All rights reserved. Terms of Use</span>
    <span>P.O.Box 41967</span>
  </div>
</footer>

</body>
</html>
```